Swift TECH Talentline by graduating students from college in two years

Based on the logo design, create stationary and business cards for
Dr. Velmor T Quenby, CEO, (555) 412-3076
and Lorna Pettigrew, Respresentative, (555) 238-6041
Address: 4197 Thistlemoor Lane, Marlow Heights, OR 97031
Incorporate elelments of the logo

Target Market(s)

USA

Font styles to use
Other font styles liked:
• match with the logo type style

```html
<!DOCTYPE html>
<html lang="en">
<head>
<meta charset="utf-8">
<title>Swift TECH Talentline – Letterhead</title>
<link href="https://fonts.googleapis.com/css2?family=EB+Garamond:wght@400;600;700&family=Lato:wght@400;700&display=swap" rel="stylesheet">
<style>
  :root {
    --navy: #1c2657;
    --gold: #f4c12e;
    --paper: #fafafb;
    --backdrop: #cecece;
    --ink: #111111;
    --body-ink: #5a5a60;
    --date-ink: #6b6b70;
    --white: #ffffff;
  }
  * { margin: 0; padding: 0; box-sizing: border-box; }
  html, body { width: 1200px; height: 840px; overflow: hidden; background: var(--backdrop); }
  .canvas { position: relative; width: 1200px; height: 840px; }

  .sheet {
    position: absolute; top: 96px; width: 495px; height: 648px;
    background: var(--paper); overflow: hidden;
  }
  .sheet--letter { left: 86px; }
  .sheet--blank { left: 619px; }

  .sheet__bands { position: absolute; inset: 0; width: 495px; height: 648px; }

  .brand-seal {
    position: absolute; left: 48px; top: 20px; width: 86px; height: 86px;
    border-radius: 50%; background: var(--white);
    border: 4px solid var(--gold);
    display: flex; align-items: center; justify-content: center; text-align: center;
    font-family: "EB Garamond", serif; font-weight: 700; font-size: 9px; line-height: 1.15;
    color: var(--navy); text-transform: uppercase; padding: 8px;
  }

  .org {
    position: absolute; left: 235px; top: 42px;
    font-family: "EB Garamond", serif; color: var(--ink); font-size: 8.2px; line-height: 11px;
  }
  .org__name { color: var(--navy); font-weight: 700; text-transform: uppercase; font-size: 7.4px; line-height: 10px; }
  .org__address { margin-top: 1px; }

  .contacts {
    position: absolute; left: 339px; top: 44px; height: 45px;
    border-left: 1.2px solid var(--navy); padding-left: 6px;
    font-family: "EB Garamond", serif; font-size: 8.2px; line-height: 12px; color: var(--ink);
  }
  .contacts__person { color: var(--navy); font-weight: 700; font-size: 9px; }
  .contacts__phone { display: flex; align-items: center; gap: 3px; }
  .contacts__phone svg { width: 7px; height: 6px; fill: var(--navy); }

  .letter { position: absolute; left: 52px; width: 391px; font-family: "Lato", sans-serif; }
  .letter__recipient { top: 175px; color: var(--ink); }
  .letter__recipient-name { font-size: 9.6px; font-weight: 700; line-height: 13px; }
  .letter__recipient-role { font-size: 7px; font-weight: 700; line-height: 11px; }
  .letter__date { position: absolute; right: 0; top: 12px; font-size: 7px; color: var(--date-ink); }

  .letter__body { top: 221px; font-size: 7.1px; line-height: 11.5px; color: var(--body-ink); text-align: justify; }
  .letter__body p + p { margin-top: 11.5px; }

  .letter__signature {
    position: absolute; left: 52px; top: 482px; width: 132px; height: 22px;
    background: linear-gradient(90deg, #e4e4e8, #f0f0f3);
    border-radius: 2px;
  }
  .letter__signer { top: 524px; color: var(--ink); }
  .letter__signer-name { font-size: 9.6px; font-weight: 700; line-height: 13px; }
  .letter__signer-role { font-size: 7px; font-weight: 700; line-height: 11px; color: #555; }

  .page-number {
    position: absolute; left: 453px; top: 622px;
    font-family: "EB Garamond", serif; font-size: 8px; color: var(--white);
  }
</style>
</head>
<body>
<main class="canvas">

  <section class="sheet sheet--letter">
    <svg class="sheet__bands" viewBox="0 0 948 1239" preserveAspectRatio="none" aria-hidden="true">
      <path fill="var(--navy)" d="M0 0H948V45Q480 10 0 150Z"/>
      <path fill="var(--gold)" d="M0 215Q420 40 948 54Q480 25 0 168Z"/>
      <path fill="var(--gold)" d="M30 1180Q520 1205 948 1106V1130Q520 1222 30 1180Z"/>
      <path fill="var(--navy)" d="M0 1182Q520 1222 948 1143V1239H0Z"/>
    </svg>

    <div class="brand-seal">Swift TECH Talentline</div>

    <div class="org">
      <div class="org__name">Swift TECH Talentline<br>2- Year Graduation</div>
      <div class="org__address">4197 Thistlemoor Lane<br>Marlow Heights, OR 97031</div>
    </div>

    <div class="contacts">
      <div class="contacts__person">Dr. Velmor T Quenby, CEO</div>
      <div class="contacts__phone"><svg viewBox="0 0 14 12"><path d="M1 4Q7 -1 13 4L11 6 9 4H5L3 6Z M3 7H11L12 11H2Z"/></svg>(555) 412-3076</div>
      <div class="contacts__person">Lorna Pettigrew, Respresentative</div>
      <div class="contacts__phone"><svg viewBox="0 0 14 12"><path d="M1 4Q7 -1 13 4L11 6 9 4H5L3 6Z M3 7H11L12 11H2Z"/></svg>(555) 238-6041</div>
    </div>

    <div class="letter letter__recipient">
      <div class="letter__recipient-name">Dear. Mrs Jane Ellis Porter</div>
      <div class="letter__recipient-role">Chief Director</div>
      <div class="letter__date">Date: 24-february-2025</div>
    </div>

    <div class="letter letter__body">
      <p>Lorem ipsum dolor sit amet, consectetur adipiscing elit, sed do eiusmod tempor incididunt ut labore et dolore magna aliqua. Sollicitudin ac orci phasellus egestas tellus rutrum tellus. Euismod elementum nisi quis eleifend quam adipiscing vitae proin sagittis. Egestas sed tempus urna et pharetra pharetra. Quis blandit turpis cursus in hac habitasse. Sed velit dignissim sodales ut eu. Ac auctor augue mauris augue neque. In arcu cursus euismod quis viverra nibh cras pulvinar mattis. Libero justo laoreet sit amet. Felis eget nunc lobortis mattis aliquam faucibus purus in. Pulvinar etiam non quam lacus suspendisse faucibus. Odio tempor orci dapibus ultrices. Velit dignissim sodales ut eu sem integer vitae justo. Fermentum et sollicitudin ac orci phasellus egestas. Pharetra vel turpis nunc eget lorem dolor sed. Sed turpis tincidunt id aliquet risus feugiat in ante. Mus mauris vitae ultricies leo integer malesuada nunc vel. Rhoncus urna neque viverra justo nec ultrices dui. Ut placerat orci nulla pellentesque dignissim enim sit amet.</p>
      <p>Bibendum arcu vitae elementum curabitur vitae nunc. Nunc pulvinar sapien et ligula ullamcorper malesuada. At elementum eu facilisis sed. Erat pellentesque adipiscing commodo elit at imperdiet dui accumsan sit. Nunc scelerisque viverra mauris in aliquam sem fringilla. In vitae turpis massa sed. Volutpat ac tincidunt vitae semper quis lectus nulla at. Massa placerat duis ultricies lacus sed turpis. Dui vivamus arcu felis bibendum ut tristique et egestas. Blandit aliquam etiam erat velit scelerisque in dictum non consectetur. Id neque aliquam vestibulum morbi blandit cursus risus at. Sed egestas egestas fringilla phasellus faucibus scelerisque eleifend donec. Ornare quam viverra orci sagittis eu volutpat odio facilisis. Volutpat sed cras ornare arcu dui vivamus arcu. Interdum consectetur libero id faucibus nisl.</p>
      <p>Viverra mauris in aliquam sem. Mattis molestie a iaculis at erat pellentesque adipiscing commodo elit. Sit amet volutpat consequat mauris nunc. Aliquam nulla facilisi cras fermentum. Sed turpis tincidunt id aliquet risus feugiat. Augue neque gravida in fermentum et sollicitudin ac orci.</p>
    </div>

    <div class="letter__signature" role="img" aria-label="Handwritten signature of Martin Cole Avery"></div>

    <div class="letter letter__signer">
      <div class="letter__signer-name">Martin Cole Avery</div>
      <div class="letter__signer-role">Chief Director</div>
    </div>
  </section>

  <section class="sheet sheet--blank">
    <svg class="sheet__bands" viewBox="0 0 948 1239" preserveAspectRatio="none" aria-hidden="true">
      <path fill="var(--navy)" d="M0 0H948V45Q480 10 0 150Z"/>
      <path fill="var(--gold)" d="M0 215Q420 40 948 54Q480 25 0 168Z"/>
      <path fill="var(--gold)" d="M30 1180Q520 1205 948 1106V1130Q520 1222 30 1180Z"/>
      <path fill="var(--navy)" d="M0 1182Q520 1222 948 1143V1239H0Z"/>
    </svg>

    <div class="brand-seal">Swift TECH Talentline</div>

    <div class="org">
      <div class="org__name">Swift TECH Talentline<br>2- Year Graduation</div>
      <div class="org__address">4197 Thistlemoor Lane<br>Marlow Heights, OR 97031</div>
    </div>

    <div class="contacts">
      <div class="contacts__person">Dr. Velmor T Quenby, CEO</div>
      <div class="contacts__phone"><svg viewBox="0 0 14 12"><path d="M1 4Q7 -1 13 4L11 6 9 4H5L3 6Z M3 7H11L12 11H2Z"/></svg>(555) 412-3076</div>
      <div class="contacts__person">Lorna Pettigrew, Respresentative</div>
      <div class="contacts__phone"><svg viewBox="0 0 14 12"><path d="M1 4Q7 -1 13 4L11 6 9 4H5L3 6Z M3 7H11L12 11H2Z"/></svg>(555) 238-6041</div>
    </div>

    <div class="page-number">1</div>
  </section>

</main>
</body>
</html>
```